Tarvell homes and renovations business card design.

Would like some new card designs utilizing my new logo that look professional. I am open to different colors on the logo or utilize the same ones we have. I like the original concept but would like to see some fresh ideas and build on what we have already done.

Target Market(s)

Custom home building industry, Real estate sales, Renovation projects.

Industry/Entity Type

Home Builder

Contact Information for Business Card

Tarvell Homes and Renovations
2871 162nd Street
Frank, Alberta
T0L3P0
Home : 403- 555-0187 Cell: 403- 555-0243

My info is : Gus Tarvell, President and CEO
email: tarvellhomes@quillmail.example
Website: tarvellhomes.example

Requirements
Must have
• Must Use my new logo design. I am open to different colors on the logo or utilize the same ones in the existing design. I can upload the original logo design if needed.

```html
<!DOCTYPE html>
<html lang="en">
<head>
<meta charset="utf-8">
<title>Tarvell Homes and Renovations – Business Card</title>
<link href="https://fonts.googleapis.com/css2?family=Open+Sans:wght@400;600&display=swap" rel="stylesheet">
<style>
  :root {
    --backdrop: #e8e3db;
    --frost-light: #f4f4f3;
    --frost-mid: #dcdcdc;
    --panel-black: #0b0b0b;
    --panel-edge: #1e1e1e;
    --accent-orange: #e07d12;
    --accent-amber: #f2a02a;
    --brand-brown: #7b5630;
    --text-soft: #d9d9d9;
  }
  html, body {
    margin: 0;
    padding: 0;
    width: 1200px;
    height: 1200px;
    overflow: hidden;
    background: var(--backdrop);
    font-family: "Open Sans", Arial, sans-serif;
  }
  .canvas {
    position: relative;
    width: 1200px;
    height: 1200px;
  }
  .card {
    position: absolute;
    left: 80px;
    top: 305px;
    width: 1040px;
    height: 590px;
    border-radius: 28px;
    overflow: hidden;
    box-shadow: 0 14px 40px rgba(0,0,0,0.18);
  }
  .card-shape {
    position: absolute;
    inset: 0;
    width: 1040px;
    height: 590px;
  }
  .brand-name {
    position: absolute;
    left: 36px;
    width: 480px;
    top: 322px;
    text-align: center;
    color: var(--brand-brown);
    font-weight: 600;
    margin: 0;
    line-height: 1;
  }
  .brand-name .brand-main {
    display: block;
    font-size: 60px;
    letter-spacing: 1px;
  }
  .brand-name .brand-sub {
    display: block;
    font-size: 20px;
    letter-spacing: 1px;
    margin-top: 8px;
  }
  .contact {
    position: absolute;
    left: 628px;
    top: 140px;
    color: var(--text-soft);
  }
  .contact-name {
    margin: 0;
    font-size: 31px;
    font-weight: 400;
    color: var(--accent-orange);
    line-height: 1.2;
  }
  .contact-title {
    margin: 0 0 18px;
    font-size: 23px;
    line-height: 1.2;
  }
  .contact-address {
    margin: 0 0 20px;
    font-size: 23px;
    line-height: 30px;
    font-style: normal;
  }
  .contact-lines {
    list-style: none;
    margin: 0;
    padding: 0;
    font-size: 23px;
    line-height: 33px;
  }
  .contact-lines li {
    display: flex;
    align-items: center;
  }
  .contact-lines svg {
    width: 20px;
    height: 20px;
    margin-right: 14px;
    fill: var(--accent-orange);
    flex: none;
  }
</style>
</head>
<body>
<main class="canvas">
  <section class="card" aria-label="Business card">
    <svg class="card-shape" viewBox="0 0 1040 590" aria-hidden="true">
      <defs>
        <linearGradient id="frost" x1="0" y1="0" x2="1" y2="1">
          <stop offset="0" stop-color="#f6f6f5"/>
          <stop offset="0.5" stop-color="#e9eaeb"/>
          <stop offset="1" stop-color="#d8d4d2"/>
        </linearGradient>
        <linearGradient id="panel" x1="0" y1="0" x2="1" y2="1">
          <stop offset="0" stop-color="#050505"/>
          <stop offset="0.6" stop-color="#121212"/>
          <stop offset="1" stop-color="#050505"/>
        </linearGradient>
        <linearGradient id="edge" x1="0" y1="0" x2="0" y2="1">
          <stop offset="0" stop-color="#a9560a"/>
          <stop offset="0.5" stop-color="#f2a02a"/>
          <stop offset="1" stop-color="#e07d12"/>
        </linearGradient>
      </defs>
      <rect class="frost-area" width="1040" height="590" fill="url(#frost)"/>
      <path class="accent-wave" d="M543 0 C 505 60, 480 140, 530 230 C 585 330, 560 470, 450 590 L 1040 590 L 1040 0 Z" fill="url(#edge)"/>
      <path class="dark-panel" d="M555 0 C 520 60, 500 140, 548 230 C 600 330, 578 470, 468 590 L 1040 590 L 1040 0 Z" fill="url(#panel)"/>
    </svg>

    <h1 class="brand-name">
      <span class="brand-main">TARVELL</span>
      <span class="brand-sub">HOMES AND RENOVATIONS</span>
    </h1>

    <div class="contact">
      <h2 class="contact-name">Gus Tarvell</h2>
      <p class="contact-title">President &amp;CEO</p>
      <address class="contact-address">2871 162nd Street<br>Frank, Alberta, T0L3P0</address>
      <ul class="contact-lines">
        <li><svg viewBox="0 0 20 20"><path d="M5 2l3 4-2 2c1 2 3 4 5 5l2-2 4 3-2 3C9 17 3 11 2 5z"/></svg>403- 555-0187</li>
        <li><svg viewBox="0 0 20 20"><path d="M6 1h8a1 1 0 0 1 1 1v16a1 1 0 0 1-1 1H6a1 1 0 0 1-1-1V2a1 1 0 0 1 1-1zm1 3v11h6V4z"/></svg>403- 555-0243</li>
        <li><svg viewBox="0 0 20 20"><path d="M1 4h18v12H1zm2 2v.5l7 5 7-5V6l-7 5z"/></svg>tarvellhomes@quillmail.example</li>
        <li><svg viewBox="0 0 20 20"><path d="M10 1a9 9 0 1 0 0 18 9 9 0 0 0 0-18zm0 2c1 0 2 2 2.4 5H7.6C8 5 9 3 10 3zM3.2 10h3.3c0 2 .4 4 1 5.3A7 7 0 0 1 3.2 10zm10.3 0h3.3a7 7 0 0 1-4.3 5.3c.6-1.3 1-3.3 1-5.3z"/></svg>tarvellhomes.example</li>
      </ul>
    </div>
  </section>
</main>
</body>
</html>
```